Business card design needed for Renewable utilities company based in New Zealand.

We supply and install solar panels and all components along with it for a fully customisable PV system that helps customer save money on their energy bills right away and also save the planet!

I have attached logo & website design files to give you a better insight.

Industry/Entity Type

Business

```html
<!DOCTYPE html>
<html lang="en">
<head>
<meta charset="utf-8">
<title>Clearsky Power – Business Card</title>
<link href="https://fonts.googleapis.com/css2?family=Questrial&display=swap" rel="stylesheet">
<style>
  :root {
    --stage: #c9c8c8;
    --card: #000000;
    --edge: #2b7ea3;
    --glow: #3a9cc8;
    --brand: #3d9fd6;
    --mark-grey: #5e5e5e;
    --mark-grey-light: #8a8a8a;
    --dot: #0d2a3d;
  }
  * { box-sizing: border-box; margin: 0; padding: 0; }
  html, body {
    width: 1200px;
    height: 1000px;
    overflow: hidden;
  }
  body {
    background: linear-gradient(180deg, #dcdcdc 0%, var(--stage) 55%, #a9a7a7 100%);
    font-family: "Questrial", "Century Gothic", sans-serif;
    display: flex;
    align-items: center;
    justify-content: center;
    gap: 60px;
  }
  .card {
    width: 500px;
    height: 290px;
    background: var(--card);
    border: 14px solid var(--edge);
    box-shadow: inset 0 0 34px 10px rgba(58, 156, 200, 0.75),
                0 6px 14px rgba(0, 0, 0, 0.35);
    position: relative;
    display: flex;
    align-items: center;
    justify-content: center;
  }
  .card-front .brand-lockup {
    display: flex;
    flex-direction: column;
    align-items: center;
    gap: 16px;
  }
  .brand-disc {
    width: 130px;
    height: 130px;
    border-radius: 50%;
    background: radial-gradient(circle at 35% 35%, var(--mark-grey-light), var(--mark-grey) 70%);
  }
  .card-front .brand-name {
    color: var(--mark-grey-light);
    font-size: 28px;
  }
  .card-back .contact-block {
    display: flex;
    align-items: center;
    gap: 16px;
    margin-left: -10px;
  }
  .brand-dot {
    width: 50px;
    height: 50px;
    border-radius: 50%;
    background: var(--brand);
    flex-shrink: 0;
  }
  .contact-text {
    display: flex;
    flex-direction: column;
    align-items: center;
    line-height: 1.05;
  }
  .card-back .brand-name {
    color: var(--brand);
    font-size: 31px;
  }
  .phone {
    color: var(--brand);
    font-size: 25px;
    letter-spacing: 0.5px;
  }
  .social-row {
    position: absolute;
    right: 14px;
    bottom: 12px;
    display: flex;
    gap: 5px;
  }
  .social-dot {
    width: 12px;
    height: 12px;
    border-radius: 50%;
    border: 1px solid var(--glow);
    background: var(--dot);
  }
</style>
</head>
<body>
  <section class="card card-front" aria-label="Card front">
    <div class="brand-lockup">
      <div class="brand-disc"></div>
      <span class="brand-name">Clearsky Power</span>
    </div>
  </section>

  <section class="card card-back" aria-label="Card back">
    <div class="contact-block">
      <div class="brand-dot"></div>
      <div class="contact-text">
        <span class="brand-name">Clearsky Power</span>
        <span class="phone">0 800 555 0142</span>
      </div>
    </div>
    <div class="social-row" aria-label="Social links">
      <span class="social-dot"></span>
      <span class="social-dot"></span>
      <span class="social-dot"></span>
      <span class="social-dot"></span>
    </div>
  </section>
</body>
</html>
```